Research Report on Media Literacy Needs a Design

We've got a cool story to tell about an innovative process of teacher professional development in media literacy education. We have a 20 page report about the work. We're looking for a designer to give it a simple but attractive look so we can publish it online.

Teacher

```html
<!DOCTYPE html>
<html lang="en">
<head>
<meta charset="utf-8">
<title>Media and Information Literacy – Page 05</title>
<link href="https://fonts.googleapis.com/css2?family=Raleway:ital,wght@0,400;0,500;0,600;1,400&display=swap" rel="stylesheet">
<style>
  :root {
    --ink: #2e2e2e;
    --brand-blue: #3a93d0;
    --paper: #ffffff;
    --on-blue: #ffffff;
  }
  * { margin: 0; padding: 0; box-sizing: border-box; }
  html, body { width: 927px; height: 1200px; overflow: hidden; background: var(--paper); }
  .page {
    position: relative;
    width: 927px;
    height: 1200px;
    font-family: "Raleway", Arial, sans-serif;
    color: var(--ink);
    font-size: 17.2px;
    line-height: 25.6px;
  }
  .column { position: absolute; }
  .column p { margin-bottom: 12px; }
  .column--left { left: 107px; top: 131px; width: 344px; }
  .column--right-top { left: 490px; top: 131px; width: 372px; }
  .column--right-bottom { left: 490px; top: 711px; width: 372px; }
  .point { position: relative; margin-top: 14px; }
  .point__tick { position: absolute; left: -21px; top: 6px; width: 15px; height: 13px; }
  .point__lead { font-style: italic; }
  .pull-quote {
    position: absolute;
    left: 490px;
    top: 432px;
    width: 437px;
    height: 263px;
    background: var(--brand-blue);
    clip-path: polygon(0 0, 420px 0, 437px 16px, 437px 242px, 417px 263px, 0 263px);
    color: var(--on-blue);
    padding: 22px 40px 0 51px;
  }
  .pull-quote__text { font-size: 21.6px; line-height: 27.3px; position: relative; }
  .pull-quote__mark { font-weight: 600; font-size: 40px; line-height: 0; position: relative; top: 12px; }
  .pull-quote__mark--open { position: absolute; left: -18px; top: 14px; }
  .pull-quote__source { font-style: italic; font-size: 19px; text-align: right; margin-top: 10px; padding-right: 8px; }
  .page-footer { position: absolute; left: 0; top: 1154px; width: 927px; height: 26px; }
  .page-footer__rule { position: absolute; left: 0; top: 12px; width: 521px; height: 1.5px; background: var(--brand-blue); }
  .page-footer__title { position: absolute; left: 528px; top: 1px; font-size: 16px; font-weight: 500; color: var(--brand-blue); letter-spacing: 0.3px; }
  .page-footer__number { position: absolute; left: 859px; top: 0; width: 68px; height: 23px; background: var(--brand-blue); color: var(--on-blue); font-weight: 600; font-size: 16px; line-height: 23px; text-align: center; }
</style>
</head>
<body>
<div class="page">
  <section class="column column--left">
    <p>both the structure and implementation process of professional development at Harbor Ridge School. As this report shows, important shifts occurred in the planning and implementation process, including the movement away from our intended plan of curriculum mapping and identification of learning targets to a more fluid, flexible and generative approach that used the identification of MIL in existing curriculum, lesson plan tagging, the blending of MIL with other competencies and literacies essential to learning at Harbor Ridge School, and a committee-led share-out of ideas as a professional development program for the full faculty.</p>
    <p class="point">
      <svg class="point__tick" viewBox="0 0 15 13" aria-hidden="true"><path d="M1.5 7 L5.5 11 L13.5 1.5" fill="none" stroke="#3a93d0" stroke-width="2.6" stroke-linecap="round" stroke-linejoin="round"/></svg>
      <span class="point__lead">The use of creative tactical strategies to accomplish practical goals through blended learning.</span> Rather than simply drop knowledge on Harbor Ridge School faculty, the Learning Media Studio team worked to identify a clear and specific goal for the engagement, adjusting our own approaches to support collaboration. To sustain a six-month, bi-coastal partnership, this professional development program used blended learning that included two intensive face-to-face meetings and several forms of intense online engagement, including teleconferencing, cloud-based collaboration, and the use of online tagging taxonomies to extend learning outside the walls of Harbor Ridge School and continue learning consistently between face-to-face sessions.
    </p>
  </section>

  <section class="column column--right-top">
    <p>Our challenge was to support the Harbor Ridge School faculty, enabling them to converge on a suitable definition of media and information literacy, activate their creative, collaborative development of lessons and projects informed by media and information literacy, and extend any professional development insights into an ongoing process of building and sharing MIL practices across subjects and grade levels.</p>
  </section>

  <blockquote class="pull-quote">
    <p class="pull-quote__text"><span class="pull-quote__mark pull-quote__mark--open">“</span>Media and information literacy is an expanded conceptualization of literacy that includes the ability to access, analyze, compose, reflect and take action using media texts, tools and technologies in a wide variety of forms<span class="pull-quote__mark">”</span></p>
    <p class="pull-quote__source">—Elena Marsh</p>
  </blockquote>

  <section class="column column--right-bottom">
    <p>In the process, we discovered the faculty’s existing understandings of media and information literacy and pushed them further within their own contexts. This process of discovery and flexibility required several key shifts from standard top-down professional development models and through a process Marsh and Whitfield have called messy engagement. When staff development (like other forms of teaching and learning) activates engagement, collaboration, creativity, innovation, and risk-taking, it can be messy at times. Rather than focusing</p>
  </section>

  <footer class="page-footer">
    <div class="page-footer__rule"></div>
    <div class="page-footer__title">MEDIA AND INFORMATION LITERACY</div>
    <div class="page-footer__number">Pg 05</div>
  </footer>
</div>
</body>
</html>
```